Personal Training

The name of my company is Heron Vitality. I am looking for a design that will feature the 8 components I am utilizing in my workouts (strength, flexibility, agility, core, power, balance, cardiovacular, speed) and represent the spider. It is not essesstial to have a spider for my logo but would be nice. If a spider is used please do not use a logo like Crowlord, a tarantula, or anything scary involving a spider (I have female clients who would get scared) lol
If you need me to provide more information please let me know. Feel free to check my website for ideas but ignore the pictures on my site as those are not pictures of me or clients
Thank you in advance!

Industry/Entity Type

Fitness

Contact Information for Business Card

Dale Presky
Company Name: Heron Vitality
Tag line: 8 components to a better you
Website: hervit7.example
Email: dale@hervit7.example
Cell: 555-413-2086

KPTB Certified Personal Trainer
CPR AED Northern Pulse Council
B.A. Exercise Physiology W.L.M., 2004

```html
<!DOCTYPE html>
<html lang="en">
<head>
<meta charset="utf-8">
<title>Heron Vitality – Business Card</title>
<link href="https://fonts.googleapis.com/css2?family=Arimo:wght@400;700&family=Tinos:ital,wght@1,700&display=swap" rel="stylesheet">
<style>
  :root {
    --backdrop: #dcdcdc;
    --card-white: #ffffff;
    --card-black: #000000;
    --brand-red: #d64545;
    --accent-red: #e0232b;
    --ink: #222222;
    --ink-light: #ffffff;
    --bar-grey: #a9a9a9;
  }
  * { margin: 0; padding: 0; box-sizing: border-box; }
  html, body {
    width: 1200px; height: 960px; overflow: hidden;
    background: var(--backdrop);
    font-family: "Arimo", Arial, sans-serif;
  }
  .canvas { position: relative; width: 1200px; height: 960px; }

  .card {
    position: absolute; width: 640px; height: 365px;
    border-radius: 22px; overflow: hidden;
    box-shadow: 0 4px 10px rgba(0,0,0,.25);
  }

  /* Front */
  .card-front { left: 90px; top: 70px; background: var(--card-white); }
  .front-mark {
    position: absolute; left: 50%; top: 48px; transform: translateX(-50%);
    width: 130px; height: 130px; border-radius: 50%;
    background: var(--brand-red);
  }
  .front-name {
    position: absolute; left: 0; right: 0; top: 196px; text-align: center;
    font-weight: 700; font-size: 15px; letter-spacing: .5px; color: var(--ink);
  }
  .tagline {
    position: absolute; left: 0; right: 0; top: 220px;
    display: flex; justify-content: center; align-items: center; gap: 8px;
    font-family: "Tinos", "Times New Roman", serif; font-style: italic; font-weight: 700;
    font-size: 16px; color: var(--ink);
  }
  .tagline .highlight { color: var(--accent-red); }
  .bars { display: inline-flex; gap: 2px; }
  .bars i { display: block; width: 4px; height: 11px; }
  .bars i:nth-child(1) { background: var(--bar-grey); }
  .bars i:nth-child(2) { background: var(--accent-red); }
  .bars.reverse i:nth-child(1) { background: var(--accent-red); }
  .bars.reverse i:nth-child(2) { background: var(--bar-grey); }
  .rule {
    position: absolute; left: 40px; right: 40px; height: 1px;
    background: linear-gradient(90deg, transparent, var(--accent-red) 50%, transparent);
  }
  .card-front .rule { top: 300px; opacity: .7; }

  /* Back */
  .card-back { left: 470px; top: 500px; background: var(--card-black); color: var(--ink-light); }
  .holder {
    position: absolute; left: 14px; top: 14px;
    display: flex; align-items: center; gap: 6px; font-size: 15px;
  }
  .holder .surname { color: var(--accent-red); }
  .holder .bars i { height: 12px; }
  .holder .bars i:nth-child(1), .holder .bars i:nth-child(2) { background: var(--bar-grey); }
  .holder .bars i:nth-child(2) { background: #e8e8e8; }
  .credentials {
    position: absolute; left: 52px; top: 38px;
    list-style: none; font-size: 12.5px; line-height: 15px;
  }
  .contacts {
    position: absolute; left: 56px; top: 130px; list-style: none;
  }
  .contacts li {
    display: flex; align-items: center; gap: 12px;
    height: 30px; font-size: 12.5px;
  }
  .contacts svg { width: 26px; height: 26px; flex: none; }
  .back-mark {
    position: absolute; left: 418px; top: 115px;
    width: 130px; height: 130px; border-radius: 50%; background: var(--brand-red);
  }
  .back-name {
    position: absolute; left: 393px; width: 180px; top: 252px;
    text-align: center; font-size: 8px; letter-spacing: .3px;
  }
  .card-back .rule { top: 308px; opacity: .55; }
</style>
</head>
<body>
<main class="canvas">

  <section class="card card-front">
    <div class="front-mark"></div>
    <p class="front-name">HERON VITALITY</p>
    <p class="tagline">
      <span class="bars"><i></i><i></i></span>
      <span>8 Components To A Better <span class="highlight">You</span></span>
      <span class="bars reverse"><i></i><i></i></span>
    </p>
    <div class="rule"></div>
  </section>

  <section class="card card-back">
    <p class="holder">
      <span class="bars"><i></i><i></i></span>
      <span>Dale <span class="surname">Presky</span></span>
      <span class="bars"><i></i><i></i></span>
    </p>
    <ul class="credentials">
      <li>KPTB Certified Personal Trainer</li>
      <li>CPR AED Northern Pulse Council</li>
      <li>B.A. Exercise Physiology W.L.M., 2004</li>
    </ul>

    <ul class="contacts">
      <li>
        <svg viewBox="0 0 26 26" aria-hidden="true">
          <rect x="4.5" y="4.5" width="17" height="17" transform="rotate(45 13 13)" fill="var(--brand-red)"/>
          <rect x="10" y="7" width="6" height="12" rx="1" fill="none" stroke="#fff" stroke-width="1.2"/>
          <circle cx="13" cy="17" r=".7" fill="#fff"/>
        </svg>
        <span>555-413-2086</span>
      </li>
      <li>
        <svg viewBox="0 0 26 26" aria-hidden="true">
          <rect x="4.5" y="4.5" width="17" height="17" transform="rotate(45 13 13)" fill="var(--brand-red)"/>
          <rect x="8.5" y="9.5" width="9" height="7" fill="#fff"/>
          <path d="M8.5 9.5 L13 13.5 L17.5 9.5" fill="none" stroke="var(--brand-red)" stroke-width="1"/>
        </svg>
        <span>dale@hervit7.example</span>
      </li>
      <li>
        <svg viewBox="0 0 26 26" aria-hidden="true">
          <rect x="4.5" y="4.5" width="17" height="17" transform="rotate(45 13 13)" fill="var(--brand-red)"/>
          <g fill="none" stroke="#fff" stroke-width="1">
            <circle cx="13" cy="13" r="5"/>
            <ellipse cx="13" cy="13" rx="2.2" ry="5"/>
            <line x1="8" y1="13" x2="18" y2="13"/>
          </g>
        </svg>
        <span>hervit7.example</span>
      </li>
      <li>
        <svg viewBox="0 0 26 26" aria-hidden="true">
          <rect x="4.5" y="4.5" width="17" height="17" transform="rotate(45 13 13)" fill="var(--brand-red)"/>
          <path d="M13 18.5 C10.5 15 9.5 13.5 9.5 11.5 A3.5 3.5 0 0 1 16.5 11.5 C16.5 13.5 15.5 15 13 18.5 Z" fill="#fff"/>
          <circle cx="13" cy="11.5" r="1.3" fill="var(--brand-red)"/>
        </svg>
        <span>Address... here....</span>
      </li>
    </ul>

    <div class="back-mark"></div>
    <p class="back-name">HERON VITALITY</p>
    <div class="rule"></div>
  </section>

</main>
</body>
</html>
```